Family office diagram

We need a diagram we can use on our business advisory website.

The diagram should be in the colour of the firm Hollins Advisory. We have uploaded a simple marked-up design of what we require and another design as a reference for the firm's colours.

```html
<!DOCTYPE html>
<html lang="en">
<head>
<meta charset="utf-8">
<title>Hollins Advisory Diagram</title>
<link href="https://fonts.googleapis.com/css2?family=Roboto+Condensed:wght@400;700&display=swap" rel="stylesheet">
<style>
  :root {
    --navy: #001155;
    --node: #020f55;
    --sky: #4ad5fc;
    --royal: #1a40ff;
    --orange: #ff7b00;
    --mint: #e2fdfd;
    --white: #ffffff;
  }
  html, body {
    margin: 0;
    padding: 0;
    width: 1187px;
    height: 1200px;
    overflow: hidden;
    background: var(--white);
  }
  .diagram {
    display: block;
    width: 1187px;
    height: 1200px;
    font-family: "Roboto Condensed", "Arial Narrow", sans-serif;
  }
  .panel { fill: var(--mint); }
  .title-band { fill: var(--navy); }
  .title { fill: var(--white); font-size: 74px; font-weight: 400; text-anchor: middle; }
  .node { fill: var(--node); stroke: var(--sky); stroke-width: 13; }
  .node-label { fill: var(--white); font-size: 19px; text-anchor: middle; }
  .hub { fill: var(--royal); stroke: var(--orange); stroke-width: 17; }
  .hub-label { fill: var(--white); font-size: 25px; font-weight: 700; text-anchor: middle; }
  .core { fill: var(--royal); stroke: var(--sky); stroke-width: 27; }
  .core-label { fill: var(--white); font-size: 48px; font-weight: 700; text-anchor: middle; }
  .link { stroke: var(--orange); stroke-width: 3.5; fill: none; }
</style>
</head>
<body>
<svg class="diagram" viewBox="0 0 1910 1920" preserveAspectRatio="none" xmlns="http://www.w3.org/2000/svg" aria-label="Hollins Family Office service diagram">
  <rect class="panel" x="42" y="143" width="1826" height="1742"/>
  <rect class="title-band" x="42" y="38" width="1826" height="105"/>
  <text class="title" x="955" y="115">Hollins Advisory Diagram</text>

  <!-- Links from the family office to each service hub -->
  <g class="links">
    <path class="link" d="M955 932 L953 668 M942 698 L953 668 L964 698"/>
    <path class="link" d="M797 1058 L535 1015 M564 1008 L535 1015 L561 1029"/>
    <path class="link" d="M1115 1055 L1443 993 M1412 989 L1443 993 L1416 1010"/>
    <path class="link" d="M856 1228 L690 1473 M693 1443 L690 1473 L711 1455"/>
    <path class="link" d="M1063 1222 L1268 1432 M1255 1404 L1268 1432 L1240 1419"/>
  </g>

  <!-- Wealth planning -->
  <g class="group wealth-planning">
    <circle class="hub" cx="950" cy="525" r="104"/>
    <text class="hub-label" x="950" y="518">WEALTH<tspan x="950" dy="27">PLANNING</tspan></text>
    <circle class="node" cx="968" cy="293" r="72"/><text class="node-label" x="968" y="300">RELOCATION</text>
    <circle class="node" cx="817" cy="342" r="72"/><text class="node-label" x="817" y="338">LIFE<tspan x="817" dy="21">INSURANCE</tspan></text>
    <circle class="node" cx="1115" cy="351" r="72"/><text class="node-label" x="1115" y="347">WILLS<tspan x="1115" dy="21">AND GIFTS</tspan></text>
    <circle class="node" cx="731" cy="476" r="72"/><text class="node-label" x="731" y="483">FOUNDATIONS</text>
    <circle class="node" cx="1193" cy="490" r="72"/><text class="node-label" x="1193" y="486">PRENUPTIAL<tspan x="1193" dy="21">AGREEMENTS</tspan></text>
    <circle class="node" cx="750" cy="633" r="72"/><text class="node-label" x="750" y="640">HOLDINGS</text>
    <circle class="node" cx="1165" cy="646" r="72"/><text class="node-label" x="1165" y="653">TRUSTS</text>
    <circle class="node" cx="864" cy="743" r="72"/><text class="node-label" x="864" y="729">PROPERTY<tspan x="864" dy="21">HOLDING</tspan><tspan x="864" dy="21">COMPANIES</tspan></text>
    <circle class="node" cx="1044" cy="748" r="72"/><text class="node-label" x="1044" y="755">MAX ADVICE</text>
  </g>

  <!-- Wealth management -->
  <g class="group wealth-management">
    <circle class="hub" cx="405" cy="984" r="95"/>
    <text class="hub-label" x="405" y="979">WEALTH<tspan x="405" dy="27">MANAGEMENT</tspan></text>
    <circle class="node" cx="379" cy="773" r="82"/><text class="node-label" x="379" y="748">FINANCIAL<tspan x="379" dy="21">STATEMENTS</tspan><tspan x="379" dy="21">AND</tspan><tspan x="379" dy="21">REPORTING</tspan></text>
    <circle class="node" cx="596" cy="898" r="82"/><text class="node-label" x="596" y="873">DISCRETIONARY<tspan x="596" dy="21">MANAGEMENT</tspan><tspan x="596" dy="21">AND INVESTMENT</tspan><tspan x="596" dy="21">ADVICE</tspan></text>
    <circle class="node" cx="193" cy="941" r="82"/><text class="node-label" x="193" y="916">ASSET<tspan x="193" dy="21">ALLOCATION</tspan><tspan x="193" dy="21">AND RISK</tspan><tspan x="193" dy="21">MANAGEMENT</tspan></text>
    <circle class="node" cx="295" cy="1170" r="82"/><text class="node-label" x="295" y="1166">PRIVATE<tspan x="295" dy="21">EQUITY</tspan></text>
    <circle class="node" cx="544" cy="1143" r="82"/><text class="node-label" x="544" y="1129">BANK<tspan x="544" dy="21">ACCOUNT</tspan><tspan x="544" dy="21">OPENING</tspan></text>
  </g>

  <!-- Family governance -->
  <g class="group family-governance">
    <circle class="hub" cx="1550" cy="952" r="84"/>
    <text class="hub-label" x="1550" y="946">FAMILY<tspan x="1550" dy="27">GOVERNANCE</tspan></text>
    <circle class="node" cx="1537" cy="763" r="73"/><text class="node-label" x="1537" y="756">FAMILY<tspan x="1537" dy="21">ASSEMBLY</tspan></text>
    <circle class="node" cx="1726" cy="880" r="73"/><text class="node-label" x="1726" y="875">FAMILY<tspan x="1726" dy="21">CHARTER</tspan></text>
    <circle class="node" cx="1366" cy="907" r="73"/><text class="node-label" x="1366" y="903">SUCCESING<tspan x="1366" dy="21">PLANNING</tspan></text>
    <circle class="node" cx="1451" cy="1114" r="73"/><text class="node-label" x="1451" y="1108">FAMILY<tspan x="1451" dy="21">COUNCIL</tspan></text>
    <circle class="node" cx="1673" cy="1097" r="73"/><text class="node-label" x="1673" y="1091">FAMILY<tspan x="1673" dy="21">MEDIATION</tspan></text>
  </g>

  <!-- Trust corporate services -->
  <g class="group trust-corporate">
    <circle class="hub" cx="1343" cy="1512" r="80"/>
    <text class="hub-label" x="1343" y="1495">TRUST<tspan x="1343" dy="26">CORPORATE</tspan><tspan x="1343" dy="26">SERVICES</tspan></text>
    <circle class="node" cx="1304" cy="1336" r="69"/><text class="node-label" x="1304" y="1332">SECRETARIAL<tspan x="1304" dy="21">SERVICES</tspan></text>
    <circle class="node" cx="1477" cy="1390" r="69"/><text class="node-label" x="1477" y="1392">ADMINISTRATION<tspan x="1477" dy="21">SERVICES</tspan></text>
    <circle class="node" cx="1170" cy="1457" r="69"/><text class="node-label" x="1170" y="1453">LEGAL<tspan x="1170" dy="21">SERVICES</tspan></text>
    <circle class="node" cx="1516" cy="1567" r="69"/><text class="node-label" x="1516" y="1574">SERVICES</text>
    <circle class="node" cx="1209" cy="1634" r="69"/><text class="node-label" x="1209" y="1630">MANAGEMOT<tspan x="1209" dy="21">SERVICES</tspan></text>
    <circle class="node" cx="1381" cy="1690" r="69"/><text class="node-label" x="1381" y="1686">ACCOUNTING<tspan x="1381" dy="21">SERVICES</tspan></text>
  </g>

  <!-- Charity and philanthropic activities -->
  <g class="group charity">
    <circle class="hub" cx="624" cy="1572" r="84"/>
    <text class="hub-label" x="624" y="1555">CHARITY AND<tspan x="624" dy="26">PHILANTHROPIC</tspan><tspan x="624" dy="26">ACTIVITIES</tspan></text>
    <circle class="node" cx="610" cy="1384" r="72"/><text class="node-label" x="610" y="1391">STRATEGY</text>
    <circle class="node" cx="799" cy="1502" r="72"/><text class="node-label" x="799" y="1498">EVENT<tspan x="799" dy="21">MANAGEMENT</tspan></text>
    <circle class="node" cx="441" cy="1528" r="72"/><text class="node-label" x="441" y="1503">MANAGING<tspan x="441" dy="21">AND</tspan><tspan x="441" dy="21">MONITORING</tspan><tspan x="441" dy="21">PROJECTS</tspan></text>
    <circle class="node" cx="525" cy="1733" r="72"/><text class="node-label" x="525" y="1729">Fund<tspan x="525" dy="21">Raising</tspan></text>
    <circle class="node" cx="746" cy="1716" r="72"/><text class="node-label" x="746" y="1723">Establishment</text>
  </g>

  <!-- Family office core -->
  <g class="group core-group">
    <circle class="core" cx="956" cy="1097" r="151"/>
    <text class="core-label" x="956" y="1060">HOLLINS<tspan x="956" dy="51">FAMILY</tspan><tspan x="956" dy="51">OFFICE</tspan></text>
  </g>
</svg>
</body>
</html>
```